Vistalune Web Design Project

We need a new web site for our company. Vistalune provides a range of location intelligence and marketing services to assist clients in improving their performance. On the location intelligence side we're the local partner for Orbix Terra (Charts and Globe) in South Africa, we're the local reseller and can assist company with the implementation and customization - we'll shortly receive the Orbix partner logo that should also be displayed on the Homepage. On the marketing side, we provide a range of marketing services for example Tenders, Event Management and Copy writing. The company is a blend between a mapping and marketing services company. You can have a look at the existing site at www.vistalune.co.za
Updates

Dear designers, the budget for my project has been increased to $700. Looking forward to receiving your designs. Kind regards Henrik

Dear designers - many thanks for all the great designs received to date. We'll provide feedback shortly. Kind regards Vistalune

Target Market(s)

Our target market is public and private organisations, and online customers (those with a web presence) primarily in South Africa

Industry/Entity Type

Marketing

Requirements
Must have
• I have uploaded the latest text and suggested pages at this stage. Important is that it should be easy to edit the pages in an HTML editor, e.g. Pagecraft. I suspect that the navigation will be expanded later e.g. careers, success stories - so it should be easy for me add new sections to the navigation later on. I have also uploaded the different Vistalune logo designs. Please include links on the Homepage for Terms and Conditions and PAIA - see www.vistalune.co.za - also the Copyright Note at the bottom of every page
Nice to have
• Although we're targeting corporates and government, and online customers, the site should be fresh and easy to navigate. I like the use of photographs on sites and make them look more interesting than simply text. Although we're also providing marketing services, the location intelligence (mapping) and Orbix Charts/Globe aspect are perhaps the most important part of the website.

```html
<!DOCTYPE html>
<html lang="en">
<head>
<meta charset="utf-8">
<title>Vistalune</title>
<link rel="stylesheet" href="https://fonts.googleapis.com/css2?family=Arimo:wght@400;700&family=Reenie+Beanie&display=swap">
<style>
:root{
  --page-top:#8fa3b3;
  --page-bottom:#4c6883;
  --white:#ffffff;
  --nav-text:#555b61;
  --red:#e3262d;
  --red-dark:#c0151c;
  --side-top:#c2ccd4;
  --side-bottom:#9fb0bf;
  --band:#5d7891;
  --heading-blue:#4c6d8b;
  --paper:#e6e6e4;
  --paper-line:#d3d3d1;
  --ink:#444;
  --hairline:rgba(255,255,255,.22);
}
*{margin:0;padding:0;box-sizing:border-box}
html,body{width:1200px;height:833px;overflow:hidden}
body{
  position:relative;
  font-family:"Arimo",Arial,sans-serif;
  background:linear-gradient(180deg,var(--page-top) 0%,#6b849a 45%,var(--page-bottom) 100%);
  color:var(--white);
}
.abs{position:absolute}
/* header */
.header{left:166px;top:0;width:864px;height:64px;background:var(--white)}
.sidebar{left:166px;top:64px;width:155px;height:291px;background:linear-gradient(180deg,var(--side-top),var(--side-bottom))}
.shield{left:166px;top:0;width:155px;height:134px}
.brand{left:166px;top:38px;width:155px;text-align:center;display:flex;align-items:center;justify-content:center;gap:5px;
  font-size:19px;font-weight:700;color:var(--red)}
.brand-dot{width:10px;height:10px;border-radius:50%;background:#3d3f42}
.nav{left:321px;top:0;height:64px;display:flex;align-items:center}
.nav-home{width:59px;height:64px;display:flex;align-items:center;justify-content:center;border-right:1px solid #eceeef}
.nav-item{height:64px;display:flex;align-items:center;justify-content:center;font-size:12px;font-weight:700;color:var(--nav-text);border-right:1px solid #eceeef}
.nav-contact{margin-left:4px;padding:0 4px;border-right:1px solid #eceeef;height:64px;display:flex;align-items:center}
.btn-red{display:inline-flex;align-items:center;justify-content:center;border-radius:14px;color:var(--white);font-weight:700;
  background:linear-gradient(180deg,#f24a4f,var(--red-dark))}
.search{left:857px;top:20px;width:156px;height:32px;border-radius:16px;border:1px solid #d8dcdf;background:linear-gradient(180deg,#f2f3f4,#fff);
  font-size:8px;color:#a9adb1;padding:12px 0 0 16px}
.search svg{position:absolute;right:11px;top:10px}
/* hero */
.hero{left:321px;top:64px;width:709px;height:291px;
  background:linear-gradient(100deg,#dfe6ea 0%,#9ea9b2 30%,#3e3f45 55%,#d5dde2 80%,#eef2f4 100%)}
/* news */
.news-title{left:182px;top:138px;font-size:15px;font-weight:700}
.news-rule{left:166px;top:162px;width:155px;height:1px;background:rgba(255,255,255,.5)}
.news-item{left:183px;width:135px}
.news-item h3{font-size:10.5px;font-weight:700;margin-bottom:4px}
.news-item p{font-size:8px;line-height:15px;color:#f4f6f8}
.news-meta{display:flex;align-items:center;gap:6px;margin-top:1px;font-size:8px;color:#3f4c58}
.news-meta .btn-red{width:62px;height:19px;font-size:8.5px;font-weight:400;border-radius:10px}
/* band */
.partners{left:166px;top:355px;width:155px;height:196px;background:var(--white)}
.partners h2{position:absolute;left:16px;top:22px;font-size:15px;font-weight:400;color:var(--heading-blue)}
.partner-badge{position:absolute;left:34px;top:63px;width:83px;height:83px;border:1px solid #b9c6d2;background:linear-gradient(180deg,#f7f9fb,#e3eaf1)}
.partner-badge span{position:absolute;left:0;top:22px;width:100%;height:15px;background:#2a78d0}
.about{left:366px;top:377px;width:232px}
.about h2,.contact h2{font-size:15px;font-weight:400;margin-bottom:14px}
.about p{font-size:8.5px;line-height:15px;color:#f1f4f7;margin-bottom:15px}
.btn-dark{position:absolute;left:367px;top:522px;width:96px;height:28px;border-radius:14px;font-size:11px;color:var(--white);
  display:flex;align-items:center;justify-content:center;background:linear-gradient(180deg,#6f889e,#4b6379);border:1px solid #7f97ab}
.testimonials{left:608px;top:355px;width:211px;height:190px;
  background:repeating-linear-gradient(180deg,var(--paper) 0 14px,var(--paper-line) 14px 15px);color:var(--ink)}
.testimonials h2{position:absolute;left:0;top:10px;width:100%;text-align:center;font-family:"Reenie Beanie",cursive;font-weight:400;font-size:30px;color:#333}
.testimonials p{position:absolute;left:12px;top:57px;width:194px;font-size:8.5px;line-height:15px}
.testimonials .author{position:absolute;left:12px;top:139px;font-size:8.5px;color:var(--red)}
.testimonials .author b{font-weight:700}
.pager{position:absolute;left:122px;top:161px;display:flex;gap:5px}
.pager span{width:23px;height:23px;border-radius:50%;border:1px solid #9a9a9a;font-size:10px;display:flex;align-items:center;justify-content:center;color:#333}
.pager .active{color:var(--red);font-weight:700}
.handset{left:820px;top:369px;width:44px;height:91px;border-radius:8px;transform:rotate(12deg);
  background:linear-gradient(160deg,#3a3f46,#111417)}
.contact{left:872px;top:377px;width:160px}
.contact dl{font-size:10.5px;line-height:30px;margin-left:1px;margin-top:-6px}
.contact dt{display:inline}
.contact dd{display:inline;font-weight:700;font-size:11px}
.follow{left:832px;top:493px;font-size:10.5px;font-weight:700}
.follow-rule{left:832px;top:509px;width:198px;height:1px;background:var(--hairline)}
.social{left:834px;top:518px;display:flex;gap:10px}
.social a{display:flex;align-items:center;gap:4px;font-size:9px;color:var(--white);text-decoration:none}
.social i{width:14px;height:14px;background:#3b5f94;display:block}
/* footer */
.footer-rule{left:166px;top:567px;width:864px;height:1px;background:var(--hairline)}
.footer-links{left:182px;top:583px;font-size:9px;display:flex;gap:10px}
.footer-links a{color:var(--white);text-decoration:none}
.footer-links a.underlined{text-decoration:underline}
.copyright{left:770px;top:583px;width:247px;text-align:right;font-size:8.5px}
</style>
</head>
<body>
  <div class="abs header"></div>
  <div class="abs sidebar"></div>
  <svg class="abs shield" viewBox="0 0 155 134" aria-hidden="true">
    <path d="M0 0H155V64C130 95 100 118 85 128C80 132 75 132 70 128C55 118 25 95 0 64Z" fill="#fff"/>
  </svg>
  <div class="abs brand"><span class="brand-dot"></span>Vistalune</div>

  <nav class="abs nav">
    <div class="nav-home">
      <svg width="15" height="14" viewBox="0 0 15 14" aria-label="Home"><path d="M7.5 0L15 6.5H13V14H9V9.5H6V14H2V6.5H0Z" fill="#8c9196"/></svg>
    </div>
    <div class="nav-item" style="width:87px">About Us</div>
    <div class="nav-item" style="width:84px">Servcies</div>
    <div class="nav-item" style="width:86px">Products</div>
    <div class="nav-contact"><span class="btn-red" style="width:89px;height:28px;font-size:12px">Contact Us</span></div>
  </nav>
  <div class="abs search">Search
    <svg width="11" height="11" viewBox="0 0 11 11" aria-hidden="true"><circle cx="4.5" cy="4.5" r="3.5" fill="none" stroke="#b3b7bb" stroke-width="1.5"/><path d="M7 7L10.5 10.5" stroke="#b3b7bb" stroke-width="1.8"/></svg>
  </div>

  <div class="abs hero" role="img" aria-label="Photograph of four smiling business people in suits in a bright office"></div>

  <h2 class="abs news-title">News</h2>
  <svg class="abs" style="left:295px;top:147px" width="15" height="15" viewBox="0 0 15 15" aria-hidden="true"><path d="M2 13L3 9.5L10.5 2L13 4.5L5.5 12Z" fill="#fff"/></svg>
  <div class="abs news-rule"></div>

  <article class="abs news-item" style="top:174px">
    <h3>Internet tend to repeat</h3>
    <p>But I must explain to you how all this mistaken idea of denouncing pleasure...</p>
    <div class="news-meta">13-03-2012 <span class="btn-red">Read More</span></div>
  </article>
  <article class="abs news-item" style="top:266px">
    <h3>On the other hand</h3>
    <p>But I must explain to you how all this mistaken idea of denouncing pleasure...</p>
    <div class="news-meta">13-03-2012 <span class="btn-red">Read More</span></div>
  </article>

  <section class="abs partners">
    <h2>Partners</h2>
    <div class="partner-badge" role="img" aria-label="Authorised reseller partner badge"><span></span></div>
  </section>

  <section class="abs about">
    <h2>What we do ?</h2>
    <p>On the other hand, we denounce with righteous indignation and dislike men who are so beguiled and demoralized by the charms of pleasure of the moment,</p>
    <p>so blinded by desire, that they cannot foresee the pain and trouble that are bound to ensue; and equal blame belongs to those who fail in their duty through</p>
  </section>
  <a class="btn-dark">Read more</a>

  <section class="abs testimonials">
    <h2>Testimonials</h2>
    <p>But I must explain to you how all this mistaken idea of denouncing pleasure and praising pain was born and I will give you a complete account of the system, and expound the actual teachings</p>
    <div class="author">Daniel Okafor , <b>Brightfield Company</b></div>
    <div class="pager"><span class="active">1</span><span>2</span><span>3</span></div>
  </section>

  <div class="abs handset" role="img" aria-label="Illustration of a smartphone"></div>
  <section class="abs contact">
    <h2>Contact Us</h2>
    <dl>
      <div><dt>Tel: </dt><dd>+27 81 555 0142</dd></div>
      <div><dt>Fax: </dt><dd>+27 86 555 0178</dd></div>
      <div><dt>Email: </dt><dd>info@vistalune.co.za</dd></div>
    </dl>
  </section>
  <div class="abs follow">Follow us on:</div>
  <div class="abs follow-rule"></div>
  <div class="abs social">
    <a><i></i>Friendsy</a>
    <a><i></i>Chirpa</a>
    <a><i></i>Linkora</a>
  </div>

  <div class="abs footer-rule"></div>
  <div class="abs footer-links">
    <a class="underlined">Terms and Conditions</a><span>|</span><a>PAIA</a><span>|</span><a>Carrera</a>
  </div>
  <div class="abs copyright">Copyright © 2012 by Vistalune. All Rights Reserved</div>
</body>
</html>
```